Medical Marihuana Ziplock Bag Mockup Design

We seek skilled and professional designer for medical marihuana ziplock bag packaging design. We need a modern, minimal, clean Design with the name productname: Plumo - Endproduct will be a ziplock bag (see attachment) samples.
Product may but must not contain a cannabis leaf in Design7Logo

Target Market(s)

young audience

Industry/Entity Type

Medical

Logo Text

P L U M O

Font styles to use
Serif
Sans Serif

Colors
9bcb3c
abd037
cadf82
ffc214
fece3e
fee18a
6b449b
886aae
b8a6cd

Requirements
Nice to have
• Can but must not contain a minimal cannabis leaf as abstract sign

```html
<!DOCTYPE html>
<html lang="en">
<head>
<meta charset="utf-8">
<title>Plumo – Pouch Front</title>
<link rel="stylesheet" href="https://fonts.googleapis.com/css2?family=Open+Sans:wght@400;700&display=swap">
<style>
  :root {
    --page-bg: #ffffff;
    --sun-yellow: #f0b820;
    --sun-yellow-light: #fece3e;
    --plum-purple: #6b449b;
    --plum-purple-light: #886aae;
    --lavender: #b8a6cd;
    --header-white: #ffffff;
    --zip-line: #d9d9dc;
    --ink: #0a0a0a;
    --leaf-white: #ffffff;
  }
  html, body {
    margin: 0;
    padding: 0;
    width: 1200px;
    height: 1200px;
    overflow: hidden;
    background: var(--page-bg);
  }
  .canvas {
    position: relative;
    width: 1200px;
    height: 1200px;
  }
  .pouch-front {
    position: absolute;
    left: 350px;
    top: 95px;
    width: 600px;
    height: 1000px;
    overflow: hidden;
  }
  .pouch-art {
    position: absolute;
    inset: 0;
    width: 600px;
    height: 1000px;
    display: block;
  }
  .brand-name {
    position: absolute;
    left: 0;
    width: 560px;
    top: 272px;
    margin: 0;
    text-align: center;
    font-family: "Open Sans", "Helvetica Neue", sans-serif;
    font-weight: 700;
    font-size: 100px;
    line-height: 1;
    letter-spacing: 12px;
    color: var(--ink);
  }
  .net-weight {
    position: absolute;
    left: 31px;
    top: 938px;
    margin: 0;
    font-family: "Open Sans", "Helvetica Neue", sans-serif;
    font-weight: 400;
    font-size: 26px;
    line-height: 1;
    letter-spacing: 0.5px;
    color: var(--header-white);
  }
</style>
</head>
<body>
<main class="canvas">
  <section class="pouch-front">
    <svg class="pouch-art" viewBox="0 0 600 1000" xmlns="http://www.w3.org/2000/svg">
      <defs>
        <linearGradient id="header-fade" x1="0" y1="0" x2="0" y2="1">
          <stop offset="0" stop-color="var(--header-white)" stop-opacity="1"/>
          <stop offset="0.17" stop-color="var(--header-white)" stop-opacity="1"/>
          <stop offset="0.26" stop-color="var(--header-white)" stop-opacity="0.55"/>
          <stop offset="0.36" stop-color="var(--header-white)" stop-opacity="0"/>
        </linearGradient>
        <linearGradient id="purple-tone" x1="0" y1="0" x2="0" y2="1">
          <stop offset="0.15" stop-color="var(--lavender)"/>
          <stop offset="0.45" stop-color="var(--plum-purple-light)"/>
          <stop offset="0.7" stop-color="var(--plum-purple)"/>
        </linearGradient>
        <linearGradient id="yellow-tone" x1="0" y1="0" x2="0" y2="1">
          <stop offset="0.15" stop-color="var(--sun-yellow-light)"/>
          <stop offset="0.5" stop-color="var(--sun-yellow)"/>
        </linearGradient>
        <radialGradient id="leaf-tone" cx="0.5" cy="0.55" r="0.5">
          <stop offset="0" stop-color="var(--leaf-white)" stop-opacity="0.95"/>
          <stop offset="0.7" stop-color="var(--leaf-white)" stop-opacity="0.8"/>
          <stop offset="1" stop-color="var(--leaf-white)" stop-opacity="0"/>
        </radialGradient>
      </defs>

      <rect class="panel-purple" x="0" y="0" width="600" height="1000" fill="url(#purple-tone)"/>
      <polygon class="panel-yellow" points="0,0 425,0 235,1000 0,1000" fill="url(#yellow-tone)"/>
      <rect class="header-band" x="0" y="0" width="600" height="1000" fill="url(#header-fade)"/>

      <g class="zip-seal">
        <line x1="0" y1="118" x2="600" y2="118" stroke="var(--zip-line)" stroke-width="2"/>
        <line x1="0" y1="140" x2="600" y2="140" stroke="var(--zip-line)" stroke-width="3"/>
      </g>

      <ellipse class="leaf-mark" role="img" aria-label="Minimal white cannabis leaf mark"
               cx="300" cy="700" rx="260" ry="230" fill="url(#leaf-tone)"/>
    </svg>

    <h1 class="brand-name">PLUMO</h1>
    <p class="net-weight">NET WT.&nbsp; 6g</p>
  </section>
</main>
</body>
</html>
```